Cover for Inspirational Daily Journal

This is the cover for a daily journal that will focus on inspirational content for black women. The cover should have a picture or silhouette of a black woman with a crown. The title is: "Grace in Bloom: A Year of Bright Mornings." The back won't have any words. Also the journal will be published on Pagewick.

```html
<!DOCTYPE html>
<html lang="en">
<head>
<meta charset="utf-8">
<title>Grace in Bloom: A Year of Bright Mornings — Journal Cover</title>
<link rel="stylesheet" href="https://fonts.googleapis.com/css2?family=Playfair+Display:wght@700;900&family=Cinzel:wght@500;700&display=swap">
<style>
  :root {
    --page: #ffffff;
    --gold-deep: #c9921f;
    --gold-mid: #d9a92c;
    --gold-light: #ecd04a;
    --ink: #0b0906;
    --ink-soft: #1c1710;
    --text-gold: #f1d25a;
    --text-cream: #f6f1e4;
  }
  html, body {
    margin: 0;
    padding: 0;
    width: 1200px;
    height: 2337px;
    overflow: hidden;
    background: var(--page);
  }
  .canvas {
    position: relative;
    width: 1200px;
    height: 2337px;
    background: var(--page);
  }
  .cover-spread {
    position: absolute;
    left: 90px;
    top: 788px;
    width: 1020px;
    height: 761px;
    overflow: hidden;
    background:
      radial-gradient(ellipse 55% 65% at 82% 80%, var(--gold-light) 0%, rgba(236,208,74,0) 70%),
      linear-gradient(135deg, var(--gold-mid) 0%, var(--gold-deep) 45%, var(--gold-mid) 100%);
    box-shadow: 0 18px 40px rgba(0,0,0,0.28);
  }
  .title {
    position: absolute;
    left: 545px;
    top: 42px;
    width: 440px;
    margin: 0;
    text-align: center;
    color: var(--ink);
    font-family: "Playfair Display", serif;
    font-weight: 900;
    line-height: 1;
  }
  .title-lead {
    display: block;
    font-size: 54px;
    letter-spacing: 1px;
  }
  .title-main {
    display: block;
    font-size: 112px;
    letter-spacing: -2px;
    margin-top: 4px;
  }
  .portrait {
    position: absolute;
    left: 590px;
    top: 228px;
    width: 310px;
    height: 533px;
    border-radius: 155px 155px 0 0;
    background: linear-gradient(180deg, var(--ink-soft) 0%, var(--ink) 60%);
  }
  .subtitle {
    position: absolute;
    left: 600px;
    top: 360px;
    width: 290px;
    margin: 0;
    text-align: center;
    line-height: 1;
  }
  .subtitle-year {
    display: block;
    font-family: "Playfair Display", serif;
    font-weight: 700;
    font-size: 62px;
    color: var(--text-gold);
  }
  .subtitle-middle {
    display: block;
    font-family: "Cinzel", serif;
    font-weight: 700;
    font-size: 34px;
    color: var(--text-cream);
    margin-top: 14px;
  }
  .subtitle-end {
    display: block;
    font-family: "Cinzel", serif;
    font-weight: 500;
    font-size: 27px;
    color: var(--text-gold);
    margin-top: 8px;
  }
</style>
</head>
<body>
<main class="canvas">
  <section class="cover-spread" aria-label="Journal cover, back and front">
    <h1 class="title">
      <span class="title-lead">GRACE IN</span>
      <span class="title-main">BLOOM</span>
    </h1>
    <div class="portrait" role="img" aria-label="Silhouette of a black woman in profile wearing a tall crown"></div>
    <p class="subtitle">
      <span class="subtitle-year">A YEAR</span>
      <span class="subtitle-middle">OF BRIGHT</span>
      <span class="subtitle-end">MORNINGS</span>
    </p>
  </section>
</main>
</body>
</html>
```